Website Design for Forklift Training Company

DO NOT CONTACT PRIVATELY. ONLY SUBMISSIONS HERE WILL BE CONSIDERED

I need a design for a website that offers forklift training courses.

The company offers accredited, onsite forklift training that are customized for the needs of each individual company. The company offers a variety of courses to operate forklifts and other machinary.

About: "Pembrook Lift Academy Ltd delivers bespoke onsite forklift truck operator training throught the uk.
All our instructors have a wealth of knowledge and expertise to provide your company with all your forklift truck training requirements.
Pembrook Lift Academy Ltd is registered and accredited by qkmvd standards so you can be rest assured that all forklift training is carried out the very highest standard"

I need the following pages designed:
> a) Home Page: Include a header image, ways to contact, about snippet, overview of courses, accreditation that will be received after completing the courses. (See attachments for samples)
> b) About Page
> c) Contact Us Page
> d) Course Page Template: A page that will be used as template for the courses offered. It should contain;
1. Cover image for the course
2. A description of the course
3. A table indicating the various course options
4. Course Objectives
5. What the trainee will receive after doing the course (example: a certification)

Target Market(s)

Industrial Businesses

Number of Pages Required

4 page

Colors
0054AA
0677BA
7BADD7
CADEEF
E8F1F8
0094D4
00A9DD
6FCCEA
C7EBF8
E9F6FB

Requirements
Should not have
• - No Search bar

```html
<!DOCTYPE html>
<html lang="en">
<head>
<meta charset="utf-8">
<title>Pembrook Lift Academy</title>
<link rel="stylesheet" href="https://fonts.googleapis.com/css2?family=Jost:wght@400;500;600&family=Lato:wght@400;700&family=Oswald:wght@400;500;600&display=swap">
<style>
:root{
  --blue:#0054AA;
  --blue-mid:#0677BA;
  --blue-sky:#0094D4;
  --blue-light:#7BADD7;
  --blue-pale:#E8F1F8;
  --navy:#0a1a33;
  --ink:#222;
  --text:#3a3a3a;
  --white:#fff;
  --star:#f5b400;
}
*{margin:0;padding:0;box-sizing:border-box}
html,body{width:1200px;height:4559px;overflow:hidden}
body{position:relative;background:var(--white);font-family:'Lato',sans-serif;color:var(--text)}

/* header */
.site-header{position:absolute;left:0;top:0;width:1200px;height:119px;background:var(--white)}
.brand{position:absolute;left:76px;top:42px;font-family:'Jost',sans-serif;font-weight:500;font-size:22px;color:var(--blue);white-space:nowrap}
.main-nav{position:absolute;left:531px;top:50px;display:flex;gap:35px;font-family:'Jost',sans-serif;font-size:13px;color:#333}
.main-nav a{color:inherit;text-decoration:none;position:relative}
.main-nav a.active{color:var(--blue)}
.main-nav a.active::before{content:"";position:absolute;left:0;right:0;top:-50px;height:3px;background:var(--blue)}
.call{position:absolute;left:1010px;top:40px;display:flex;align-items:center;gap:10px}
.call-icon{width:26px;height:26px;border-radius:50%;background:var(--blue);display:flex;align-items:center;justify-content:center}
.call-text{font-family:'Jost',sans-serif;font-size:11px;line-height:13px;color:#111}
.call-text span{display:block;color:var(--blue)}

/* hero */
.hero{position:absolute;left:0;top:119px;width:1200px;height:633px}
.hero-photo{position:absolute;inset:0;clip-path:polygon(0 0,100% 0,100% 87%,0 100%);
  background:linear-gradient(110deg,#8e8f92 0%,#5a5f66 30%,#2b3038 55%,#1b1f27 100%)}
.hero-stripes{position:absolute;left:0;top:0}
.hero-copy{position:absolute;left:657px;top:228px;font-family:'Oswald',sans-serif;font-weight:500;font-size:40px;line-height:56px;color:var(--white);text-transform:uppercase;white-space:nowrap}
.hero-copy .hl{background:var(--blue);padding:0 5px}
.btn{display:inline-flex;align-items:center;justify-content:center;background:var(--blue);color:var(--white);font-family:'Jost',sans-serif;font-size:13px;text-transform:uppercase;text-decoration:none}
.hero-btn{position:absolute;left:657px;top:394px;width:172px;height:50px}

/* section titles */
.section-title{position:absolute;left:0;width:1200px;text-align:center;font-family:'Jost',sans-serif;font-weight:500;font-size:33px;color:var(--ink);text-transform:uppercase;line-height:41px}
.title-rule{position:absolute;left:565px;width:70px;height:4px;background:var(--blue-mid)}

/* about */
.about-copy{position:absolute;left:115px;top:945px;width:465px;font-size:12.5px;line-height:22px;color:#333}
.about-copy p+p{margin-top:21px}
.about-btn{position:absolute;left:115px;top:1248px;width:172px;height:49px}
.photo{background:linear-gradient(135deg,#6b7078,#b7b09a 45%,#d9c94a 60%,#5c6068)}
.about-photo{position:absolute;left:625px;top:920px;width:495px;height:450px}

/* courses */
.courses-band{position:absolute;left:0;top:1505px;width:1200px;height:640px;clip-path:polygon(0 97px,1200px 5px,1200px 548px,0 637px);display:flex}
.course{width:400px;height:100%;display:flex;flex-direction:column;align-items:center;color:var(--white);text-align:center}
.course:nth-child(1){background:linear-gradient(160deg,#2a63b5,#0d4fa6);padding-top:305px;width:396px}
.course:nth-child(2){background:linear-gradient(160deg,#3b6aa4,#2c62a8);padding-top:240px;width:402px}
.course:nth-child(3){background:linear-gradient(160deg,#1ba0dc,#1490d0);padding-top:208px;width:402px}
.course h3{font-family:'Jost',sans-serif;font-weight:500;font-size:22px;line-height:27px;text-transform:uppercase}
.course ul{list-style:none;margin-top:10px;font-size:12.5px;line-height:22px}
.course .btn-outline{margin-top:18px;width:170px;height:50px;border:1.5px solid var(--white);display:flex;align-items:center;justify-content:center;font-family:'Jost',sans-serif;font-size:13px;text-transform:uppercase;color:var(--white)}

/* accreditation */
.accr-photo{position:absolute;left:104px;top:2333px;width:496px;height:449px}
.badge{position:absolute;left:487px;width:138px;height:102px;background:var(--blue-pale);display:flex;align-items:center;justify-content:center}
.badge-a{top:2580px}
.badge-b{top:2700px}
.accr-copy{position:absolute;left:657px;top:2342px;width:472px;font-size:12.5px;line-height:22px;color:#333}
.accr-copy p+p{margin-top:21px}
.accr-copy p.tight{margin-top:0}
.accr-btn{position:absolute;left:658px;top:2727px;width:172px;height:49px}

/* testimonials */
.testimonials{position:absolute;left:0;top:2870px;width:1200px;height:660px;clip-path:polygon(0 95px,1200px 6px,1200px 555px,0 652px);
  background:linear-gradient(180deg,#1a5fb8,#0c4fa8)}
.testimonials .section-title{color:var(--white);top:135px}
.avatar{position:absolute;left:538px;top:183px;width:132px;height:132px;border-radius:50%;border:4px solid var(--white);background:linear-gradient(135deg,#7a7f88,#c9b15a 60%,#3a3f48)}
.person{position:absolute;left:0;width:1200px;text-align:center;color:var(--white)}
.person-name{top:325px;font-family:'Jost',sans-serif;font-size:16px}
.person-role{top:352px;font-size:12px}
.quote{position:absolute;left:330px;top:387px;width:545px;text-align:center;color:var(--white);font-family:'Jost',sans-serif;font-size:13.5px;line-height:18px}
.quote .mark{font-family:'Lato',sans-serif;font-size:26px;font-style:italic;vertical-align:-6px;padding:0 4px}
.stars{position:absolute;left:0;width:1200px;top:466px;text-align:center;color:var(--star);font-size:13px;letter-spacing:3px}
.arrow{position:absolute;top:383px;width:42px;height:42px;border-radius:50%;background:rgba(255,255,255,.25);display:flex;align-items:center;justify-content:center}
.dots{position:absolute;left:585px;top:556px;display:flex;gap:5px}
.dots i{width:5px;height:5px;border-radius:50%;background:var(--blue-light)}
.dots i.on{background:var(--white)}

/* contact */
.contact-form{position:absolute;left:319px;top:3623px;width:584px}
.field{position:absolute;height:48px;border:1px solid #b9b9b9;font-family:'Jost',sans-serif;font-size:13px;color:#666;padding:15px 9px}
.submit{position:absolute;left:512px;top:3906px;width:171px;height:49px}
.reach{position:absolute;top:3996px;display:flex;align-items:center;gap:12px}
.reach small{display:block;font-family:'Jost',sans-serif;font-size:12px;color:var(--blue)}
.reach strong{display:block;font-family:'Jost',sans-serif;font-weight:500;font-size:22px;color:#111;line-height:24px}
.or{position:absolute;left:570px;top:3984px;width:60px;height:60px;border-radius:50%;background:var(--blue);color:var(--white);font-family:'Jost',sans-serif;font-weight:600;font-size:20px;display:flex;align-items:center;justify-content:center}

/* footer */
.footer-shape{position:absolute;left:0;top:4140px}
.foot-brand{position:absolute;left:113px;top:4305px;font-family:'Jost',sans-serif;font-weight:500;font-size:32px;line-height:46px;color:#1565c0;white-space:nowrap}
.foot-col{position:absolute;top:4287px;color:var(--white)}
.foot-col h4{font-family:'Jost',sans-serif;font-weight:500;font-size:11px;text-transform:uppercase;position:relative;padding-bottom:10px}
.foot-col h4::after{content:"";position:absolute;left:0;bottom:0;width:26px;height:2px;background:var(--white)}
.foot-links{list-style:none;margin-top:18px;font-family:'Jost',sans-serif;font-size:12px;line-height:22.5px}
.foot-links li::before{content:">";margin-right:10px}
.info{list-style:none;margin-top:18px;font-family:'Jost',sans-serif;font-size:12px}
.info li{display:flex;align-items:center;gap:12px;height:45px}
.news-input{width:260px;height:40px;margin-top:21px;background:var(--white);color:#555;font-family:'Jost',sans-serif;font-size:12px;display:flex;align-items:center;justify-content:center}
.news-btn{width:260px;height:40px;margin-top:9px}
.bottom-bar{position:absolute;left:0;top:4510px;width:1200px;height:49px;background:var(--blue);color:var(--white);font-family:'Jost',sans-serif;font-size:12px}
.bottom-bar p{position:absolute;left:113px;top:17px}
.social{position:absolute;left:953px;top:10px;display:flex;gap:6px}
.social span{width:30px;height:30px;border-radius:50%;background:var(--white)}
</style>
</head>
<body>

<header class="site-header">
  <div class="brand">Pembrook Lift Academy</div>
  <nav class="main-nav">
    <a class="active" href="#">Home</a>
    <a href="#">About us</a>
    <a href="#">Our Courses</a>
    <a href="#">Accreditation</a>
    <a href="#">Contact us</a>
  </nav>
  <div class="call">
    <div class="call-icon">
      <svg width="14" height="14" viewBox="0 0 24 24"><path fill="#fff" d="M6.6 10.8a15 15 0 0 0 6.6 6.6l2.2-2.2c.3-.3.7-.4 1-.2 1.1.4 2.3.6 3.6.6.6 0 1 .4 1 1V20c0 .6-.4 1-1 1A17 17 0 0 1 3 4c0-.6.4-1 1-1h3.5c.6 0 1 .4 1 1 0 1.3.2 2.5.6 3.6.1.3 0 .7-.2 1z"/></svg>
    </div>
    <div class="call-text"><span>Call us</span>123 456 7890</div>
  </div>
</header>

<section class="hero">
  <div class="hero-photo" role="img" aria-label="Smiling operator in a yellow hard hat seated in a forklift inside a warehouse"></div>
  <svg class="hero-stripes" width="1200" height="633" viewBox="0 0 1200 633">
    <polygon points="837,562 1200,529 1200,556 837,588" fill="#0094D4"/>
    <polygon points="1000,578 1200,556 1200,583 1000,600" fill="#0054AA"/>
  </svg>
  <div class="hero-copy">
    Get<br>
    Your <span class="hl">Team Certified</span><br>
    To Operate Your <span class="hl">Forklift</span>
  </div>
  <a class="btn hero-btn" href="#">Read more</a>
</section>

<h2 class="section-title" style="top:786px">About Us</h2>
<div class="title-rule" style="top:836px"></div>
<div class="about-copy">
  <p>Lorem Ipsum is simply dummy text of the printing and typesetting industry has been the industry's standard dummy text ever since the 1500s,</p>
  <p>when an unknown printer took a galley of type and scrambled it to make a type specimen book. It has survived not only five centuries, but also the leap into electronic typesetting, remaining essentially unchanged. It was popularised in the 1960s</p>
  <p>with the release of Lettraform sheets containing Lorem Ipsum passages, and more recently with desktop publishing software like Pagewright Studio including into electronic typesetting, remaining essentially unchanged. It was popularised versions of Lorem Ipsum.</p>
</div>
<a class="btn about-btn" href="#">Read more</a>
<div class="about-photo photo" role="img" aria-label="Two instructors in hard hats and hi-vis vests beside a forklift, one holding a clipboard"></div>

<h2 class="section-title" style="top:1479px">Courses</h2>
<section class="courses-band" role="group" aria-label="Course categories">
  <div class="course" role="img" aria-label="Blue-tinted photo of a trainee in a hard hat">
    <h3>Forklift Training<br>Courses</h3>
    <ul><li>Bendi Truck Traning Course</li><li>Combi Lift Traning Course</li><li>Counterbalance Traning Course</li></ul>
    <span class="btn-outline">Read more</span>
  </div>
  <div class="course" role="img" aria-label="Blue-tinted photo of forklifts parked in a warehouse">
    <h3>MEWP Training<br>Courses</h3>
    <ul><li>Cherry Picker Training Course</li><li>Scissor Lift Traning Course</li><li>Harness And Landard Traning Course</li></ul>
    <span class="btn-outline">Read more</span>
  </div>
  <div class="course" role="img" aria-label="Sky-blue tinted photo of workers beside a forklift">
    <h3>Other Training<br>Courses</h3>
    <ul><li>Bendi Truck Traning Course</li><li>Combi Lift Traning Course</li><li>Counterbalance Traning Course</li></ul>
    <span class="btn-outline">Read more</span>
  </div>
</section>

<h2 class="section-title" style="top:2201px">Forklift Training<br>Accreditation</h2>
<div class="accr-photo photo" role="img" aria-label="Instructor with clipboard next to a smiling trainee seated on a forklift"></div>
<div class="badge badge-a"><svg width="62" height="66"><rect width="62" height="66" fill="#1c2a6b"/></svg></div>
<div class="badge badge-b"><svg width="92" height="52"><rect width="92" height="52" rx="8" fill="#2f6f4e"/></svg></div>
<div class="accr-copy">
  <p>QKMVD is recognised throughout the united kingdom and ireland as one of the leading meterial handling equipment training accrediting bodies.</p>
  <p>QKMVD is a founder member of the FACA (accrediting bodies association for workplace transport) and his replaced the accreding bodies forum previously run by the WSA.</p>
  <p>They have over 40 year experience of setting training standards, accreditaion and monitoring.</p>
  <p class="tight">The QKMVD Accreditation schemes are supported by legal requirements for training. The health and safety at work act 1974 prescribes a legal duty to provide adequate training and instruction to their employees. This is Reinforced by the provision &amp; use of work equipment regulations of 1998 which states that using equipment, and risks and precautions taken.</p>
  <p>The QKMVD accreditation schemes and standard are guided by the approved code of practice for rider operated lift trucks.</p>
</div>
<a class="btn accr-btn" href="#">Read more</a>

<section class="testimonials">
  <h2 class="section-title">Testimonials</h2>
  <div class="avatar" role="img" aria-label="Portrait of the reviewer in a hard hat"></div>
  <div class="person person-name">Clara Wendell</div>
  <div class="person person-role">Creative Director</div>
  <div class="arrow" style="left:232px"><svg width="16" height="20"><path d="M12 2 4 10l8 8" stroke="#fff" stroke-width="2" fill="none"/></svg></div>
  <div class="arrow" style="left:929px"><svg width="16" height="20"><path d="M4 2l8 8-8 8" stroke="#fff" stroke-width="2" fill="none"/></svg></div>
  <p class="quote"><span class="mark">“</span>Lorem Ipsum&nbsp; simply dummy text the printing and ypesetting industry simply Ipsum is simply dummy text of the printing.Lorem Ipsum&nbsp; simply dummy text the simply is simply dummy text of the in the industries printing. <span class="mark">”</span></p>
  <div class="stars">★★★★★</div>
  <div class="dots"><i></i><i></i><i class="on"></i></div>
</section>

<h2 class="section-title" style="top:3548px">Contact Us</h2>
<form class="contact-form">
  <div class="field" style="left:0;top:0;width:191px">Name</div>
  <div class="field" style="left:196px;top:0;width:192px">Email</div>
  <div class="field" style="left:393px;top:0;width:191px">Phone</div>
  <div class="field" style="left:0;top:57px;width:584px">Subjects<span style="position:absolute;right:14px">v</span></div>
  <div class="field" style="left:0;top:114px;width:584px;height:140px;padding-top:8px">Message</div>
</form>
<a class="btn submit" href="#">Submit</a>
<div class="reach" style="left:354px">
  <svg width="40" height="40" viewBox="0 0 24 24"><path fill="#0054AA" d="M6.6 10.8a15 15 0 0 0 6.6 6.6l2.2-2.2c.3-.3.7-.4 1-.2 1.1.4 2.3.6 3.6.6.6 0 1 .4 1 1V20c0 .6-.4 1-1 1A17 17 0 0 1 3 4c0-.6.4-1 1-1h3.5c.6 0 1 .4 1 1 0 1.3.2 2.5.6 3.6.1.3 0 .7-.2 1z"/><path d="M15 3a6 6 0 0 1 6 6M15 6.5A2.5 2.5 0 0 1 17.5 9" stroke="#0054AA" stroke-width="1.6" fill="none"/></svg>
  <div><small>Contact us at</small><strong>123-456-7890</strong></div>
</div>
<div class="or">OR</div>
<div class="reach" style="left:655px">
  <svg width="44" height="40" viewBox="0 0 44 40"><rect x="2" y="12" width="40" height="26" fill="none" stroke="#0054AA" stroke-width="2.5"/><path d="M2 12l20 16 20-16" fill="none" stroke="#0054AA" stroke-width="2.5"/><circle cx="22" cy="10" r="8" fill="#fff" stroke="#0054AA" stroke-width="2.5"/></svg>
  <div><small>Email us</small><strong>123-456-7890</strong></div>
</div>

<svg class="footer-shape" width="1200" height="370" viewBox="0 0 1200 370">
  <polygon points="0,69 1200,0 1200,370 0,370" fill="#0a1a33"/>
  <polygon points="0,30 186,21 186,48 0,57" fill="#0094D4"/>
  <polygon points="0,52 345,36 345,62 0,78" fill="#0054AA"/>
</svg>
<div class="foot-brand">Pembrook Lift<br>Academy</div>
<div class="foot-col" style="left:409px">
  <h4>Quick links</h4>
  <ul class="foot-links"><li>Home</li><li>About us</li><li>Our Courses</li><li>Accreditatioon</li><li>Contact us</li></ul>
</div>
<div class="foot-col" style="left:614px">
  <h4>Contact info</h4>
  <ul class="info">
    <li><svg width="12" height="12" viewBox="0 0 24 24"><path fill="#fff" d="M6.6 10.8a15 15 0 0 0 6.6 6.6l2.2-2.2c.3-.3.7-.4 1-.2 1.1.4 2.3.6 3.6.6.6 0 1 .4 1 1V20c0 .6-.4 1-1 1A17 17 0 0 1 3 4c0-.6.4-1 1-1h3.5c.6 0 1 .4 1 1 0 1.3.2 2.5.6 3.6.1.3 0 .7-.2 1z"/></svg>780-555-0142</li>
    <li><svg width="13" height="10"><rect x=".5" y=".5" width="12" height="9" fill="none" stroke="#fff"/><path d="M.5 .5l6 5 6-5" fill="none" stroke="#fff"/></svg>domain@name.com</li>
    <li><svg width="12" height="14" viewBox="0 0 24 28"><path fill="#fff" d="M12 0a10 10 0 0 0-10 10c0 7.5 10 18 10 18s10-10.5 10-18A10 10 0 0 0 12 0zm0 14a4 4 0 1 1 0-8 4 4 0 0 1 0 8z"/></svg>Harrowdene, UK</li>
  </ul>
</div>
<div class="foot-col" style="left:831px">
  <h4>Newsletter</h4>
  <div class="news-input">Email address</div>
  <a class="btn news-btn" href="#">Subscribe</a>
</div>
<footer class="bottom-bar">
  <p>Copyright © 2021 <b>Pembrook Lift Academy Ltd</b>, All Rights Reserved</p>
  <div class="social" aria-label="Social links"><span></span><span></span><span></span><span></span></div>
</footer>

</body>
</html>
```